Personal Training Studio needs small flyer design

My Personal Training Studio is looking to offer local high end clothes shops the option to offer their customers free Personal Training at our studio. It will be a small flyer (more a slip - landscape) that can be put into customers shopping bags once they have purchased an item from the store.
It is being marketed as a Local Fitness Initiative which is called "Be Fit In Your Clothes" The idea is to come from a "Be Fit" health perspective but also "Fit into your clothes" from the clothes shops perspective. Perhaps the "Be" in a different colour to the rest of the title. I would like my company logo and colours to be used, plus the address of the of the studio (see website - www.harbourlane7strength.co.uk). Flyer can be double sided

Target Market(s)

High end clothing shops

Industry/Entity Type

Training

Requirements
Must have
• Reference to the fact that the voucher is offering a FREE Personal Training session. Contact us to book yours today.

```html
<!DOCTYPE html>
<html lang="en">
<head>
<meta charset="utf-8">
<title>Be Fit In Your Clothes – Flyer</title>
<link href="https://fonts.googleapis.com/css2?family=Oswald:wght@700&family=Lato:wght@300;400;700&family=Cinzel:wght@700&family=PT+Sans+Narrow:wght@400;700&display=swap" rel="stylesheet">
<style>
  :root {
    --navy: #262a6b;
    --teal: #3fc3c1;
    --teal-text: #2fb3b8;
    --header-grey: #d3d4d6;
    --band-grey: #b9bcbf;
    --body-light: #f4f4f5;
    --body-mid: #e2e3e5;
    --ink: #111111;
    --page: #e9e9ea;
  }
  * { margin: 0; padding: 0; box-sizing: border-box; }
  html, body {
    width: 1200px; height: 857px; overflow: hidden;
    background: var(--page);
  }
  .flyer {
    position: absolute; left: 40px; top: 153px;
    width: 1120px; height: 551px;
    background: linear-gradient(180deg, var(--body-light) 0%, var(--body-mid) 100%);
    overflow: hidden;
    box-shadow: 0 6px 18px rgba(0,0,0,0.18);
  }
  .flyer__accent { position: absolute; left: 0; top: 0; width: 100%; height: 20px; background: var(--teal); }
  .flyer__accent-rule { position: absolute; left: 0; top: 20px; width: 100%; height: 9px; background: var(--band-grey); }
  .headline-band {
    position: absolute; left: 0; top: 29px; width: 100%; height: 101px;
    background: linear-gradient(180deg, #cfd0d2 0%, var(--header-grey) 100%);
  }
  .headline {
    position: absolute; left: 52px; top: 34px;
    display: flex; align-items: baseline; white-space: nowrap;
  }
  .headline__be {
    font-family: 'Oswald', sans-serif; font-weight: 700;
    font-size: 94px; line-height: 1; color: var(--navy);
    letter-spacing: -2px; margin-right: 18px;
  }
  .headline__fit {
    font-family: 'Lato', sans-serif; font-weight: 400;
    font-size: 66px; color: var(--ink); margin-right: 14px; letter-spacing: -1px;
  }
  .headline__clothes {
    font-family: 'Cinzel', serif; font-weight: 700;
    font-size: 56px; color: var(--ink);
  }
  .photo-waist {
    position: absolute; left: 17px; top: 130px; width: 300px; height: 367px;
    background: linear-gradient(90deg, #c9a289 0%, #b68a6e 45%, #aac6d6 70%, #ececee 100%);
  }
  .photo-shoppers {
    position: absolute; left: 765px; top: 45px; width: 355px; height: 452px;
    background: linear-gradient(180deg, #e9d8cf 0%, #b57b6a 45%, #8a3a4c 75%, #c9c9cb 100%);
  }
  .offer {
    position: absolute; left: 330px; top: 148px; width: 425px;
    text-align: center;
  }
  .offer__title {
    font-family: 'PT Sans Narrow', sans-serif; font-weight: 400;
    font-size: 44px; color: var(--navy); line-height: 1; white-space: nowrap;
  }
  .offer__title strong {
    font-family: 'Lato', sans-serif; font-weight: 700; font-style: italic;
    font-size: 42px; margin-right: 6px;
  }
  .brand-name {
    margin: 30px auto 0; display: inline-flex; align-items: center; gap: 10px;
    font-family: 'Lato', sans-serif; font-weight: 700;
    font-size: 24px; letter-spacing: 2px; color: var(--navy);
    text-transform: uppercase;
  }
  .brand-name__square { width: 18px; height: 18px; background: var(--teal); }
  .offer__intro {
    margin-top: 30px;
    font-family: 'Lato', sans-serif; font-weight: 400;
    font-size: 17.5px; line-height: 24px; color: var(--teal-text);
  }
  .offer__phones {
    margin-top: 6px;
    font-family: 'Lato', sans-serif; font-weight: 700;
    font-size: 23.5px; line-height: 30px; color: var(--navy);
  }
  .offer__email {
    margin-top: 2px;
    font-family: 'Lato', sans-serif; font-weight: 400;
    font-size: 17px; color: var(--navy);
  }
  .footer-rule { position: absolute; left: 0; top: 484px; width: 100%; height: 2px; background: #c4c6c8; }
  .footer {
    position: absolute; left: 0; top: 497px; width: 100%; height: 54px;
    background: var(--navy);
    display: flex; align-items: center; justify-content: space-between;
    padding: 0 28px 0 24px;
  }
  .footer__address {
    display: flex; align-items: center; gap: 8px;
    font-family: 'Lato', sans-serif; font-size: 17px; color: #ffffff;
  }
  .footer__web {
    font-family: 'Lato', sans-serif; font-size: 24px; letter-spacing: 2.5px;
    color: var(--teal);
  }
</style>
</head>
<body>
  <main class="flyer">
    <div class="flyer__accent"></div>
    <div class="flyer__accent-rule"></div>
    <div class="headline-band"></div>
    <h1 class="headline">
      <span class="headline__be">Be</span>
      <span class="headline__fit">Fit In Your</span>
      <span class="headline__clothes">Clothes</span>
    </h1>

    <div class="photo-waist" role="img" aria-label="Photo of a woman measuring her slim waist with a tape measure"></div>
    <div class="photo-shoppers" role="img" aria-label="Photo of three stylish young women in fashionable clothes posing against a white wall"></div>

    <section class="offer">
      <p class="offer__title"><strong>FREE</strong> Personal Training @</p>
      <div class="brand-name"><span class="brand-name__square"></span>Harbour Lane 7 Strength</div>
      <p class="offer__intro">For a consultation with one of our Personal Trainers<br>and your free Health MOT get in touch today…</p>
      <p class="offer__phones">07700 900 318 or<br>01632 960 274 (studio)</p>
      <p class="offer__email">email : info@harbourlane7strength.co.uk</p>
    </section>

    <div class="footer-rule"></div>
    <footer class="footer">
      <span class="footer__address">
        <svg width="16" height="22" viewBox="0 0 16 22" aria-hidden="true">
          <path d="M8 0C3.6 0 0 3.4 0 7.7 0 13 8 22 8 22s8-9 8-14.3C16 3.4 12.4 0 8 0z" fill="#3fc3c1"/>
        </svg>
        7 Harbour Lane, Thornbury, North Yorkshire YO9 4QT
      </span>
      <span class="footer__web">www.harbourlane7strength.co.uk</span>
    </footer>
  </main>
</body>
</html>
```